A property investment company, looking to provide lovely sustainable homes for familys and individua

For a small investment business i am starting which will buy and refurbish unloved houses and apartments to rent out or resell. the company name is my family surname (HARGREAVE). <br/>i would like the design to be simple with maybe some emphasis on an ethical and sustainable/environmentally friendly approach with a branding of maybe trees blended with some houses and or apartments.<br/>The colours i like for this design would be mainly green on either a white or black background.
Target Market(s)
This business card is to be used for professional people such as estate agents
mortgage brokers, solicitors and trades people.
Industry/Entity Type
Real Estate
Contact Information for Business Card
owner/director-Martin hargreave
e-mail-martin@hwlettings.co.uk
website-hargreavehomeholdings.co.uk
mobile-07934560218
landline-02086543107

```html
<!DOCTYPE html>
<html lang="en">
<head>
<meta charset="utf-8">
<title>Hargreave Property Investments – Business Card</title>
<link href="https://fonts.googleapis.com/css2?family=Montserrat:wght@300;400;500&family=Roboto+Condensed:wght@700&display=swap" rel="stylesheet">
<style>
  :root {
    --backdrop: #2b2b2d;
    --card-white: #ffffff;
    --teal: #2cb49c;
    --teal-deep: #1f9983;
    --teal-light: #4cc7b1;
    --ink: #1d1d1f;
    --ink-soft: #4a4a4d;
    --on-teal: #ffffff;
  }
  * { box-sizing: border-box; margin: 0; padding: 0; }
  html, body { width: 1200px; height: 900px; overflow: hidden; }
  body {
    background: var(--backdrop);
    font-family: "Montserrat", sans-serif;
    display: flex;
    flex-direction: column;
    align-items: center;
    justify-content: center;
    gap: 44px;
  }
  .card {
    position: relative;
    width: 660px;
    height: 384px;
    overflow: hidden;
    box-shadow: 0 14px 34px rgba(0,0,0,.45);
  }

  /* Front */
  .card--front { background: var(--card-white); }
  .brand {
    position: absolute;
    font-weight: 300;
    letter-spacing: 6px;
    color: var(--ink);
  }
  .card--front .brand {
    left: 96px;
    top: 92px;
    font-size: 50px;
  }
  .owner {
    position: absolute;
    left: 96px;
    top: 222px;
    text-align: right;
    width: 230px;
  }
  .owner__name {
    font-family: "Roboto Condensed", sans-serif;
    font-weight: 700;
    font-size: 34px;
    line-height: 1;
    color: var(--ink);
  }
  .owner__name .first { color: var(--teal); }
  .owner__role {
    margin-top: 6px;
    font-size: 15px;
    letter-spacing: 3px;
    color: var(--ink-soft);
  }
  .divider {
    position: absolute;
    left: 350px;
    top: 200px;
    width: 3px;
    height: 104px;
    background: var(--teal);
  }
  .contacts {
    position: absolute;
    left: 372px;
    top: 204px;
    list-style: none;
    font-size: 14.5px;
    letter-spacing: .6px;
    color: var(--ink);
  }
  .contacts li {
    display: flex;
    align-items: center;
    gap: 8px;
    height: 30px;
    white-space: nowrap;
  }
  .contacts svg { width: 13px; height: 13px; flex: none; fill: var(--teal); }
  .contacts .sep { color: var(--ink-soft); margin: 0 2px; }

  /* Back */
  .card--back { background: var(--teal); }
  .scene {
    position: absolute;
    inset: 0;
    background: linear-gradient(120deg, var(--teal-deep) 0%, var(--teal) 45%, var(--teal-light) 100%);
  }
  .card--back .brand {
    left: 0;
    right: 0;
    top: 112px;
    text-align: center;
    font-size: 66px;
    letter-spacing: 8px;
    color: var(--on-teal);
  }
  .services {
    position: absolute;
    left: 0;
    right: 0;
    bottom: 78px;
    text-align: center;
    font-size: 24px;
    font-weight: 500;
    letter-spacing: 4px;
    color: var(--on-teal);
  }
  .services .dot {
    display: inline-block;
    width: 10px;
    height: 10px;
    border-radius: 50%;
    background: var(--on-teal);
    margin: 0 10px 3px;
  }
</style>
</head>
<body>

  <section class="card card--front">
    <div class="brand">HARGREAVE</div>

    <div class="owner">
      <p class="owner__name"><span class="first">Martin</span> Hargreave</p>
      <p class="owner__role">Owner-Director</p>
    </div>

    <div class="divider"></div>

    <ul class="contacts">
      <li>
        <svg viewBox="0 0 24 24"><path d="M6.6 10.8a15.1 15.1 0 0 0 6.6 6.6l2.2-2.2a1 1 0 0 1 1-.25 11.4 11.4 0 0 0 3.6.57 1 1 0 0 1 1 1V20a1 1 0 0 1-1 1A17 17 0 0 1 3 4a1 1 0 0 1 1-1h3.5a1 1 0 0 1 1 1c0 1.25.2 2.45.57 3.57a1 1 0 0 1-.25 1z"/></svg>
        07934560218<span class="sep">-</span>
        <svg viewBox="0 0 24 24"><path d="M7 1h10a2 2 0 0 1 2 2v18a2 2 0 0 1-2 2H7a2 2 0 0 1-2-2V3a2 2 0 0 1 2-2zm0 3v14h10V4z"/></svg>
        02086543107
      </li>
      <li>
        <svg viewBox="0 0 24 24"><path d="M2 5h20v14H2zm2 2v.5l8 5 8-5V7l-8 5z"/></svg>
        martin@hwlettings.co.uk
      </li>
      <li>
        <svg viewBox="0 0 24 24"><path d="M12 2a10 10 0 1 0 0 20 10 10 0 0 0 0-20zm6.9 6h-3a15 15 0 0 0-1.3-3.9A8 8 0 0 1 18.9 8zM12 4c.8 1.2 1.5 2.5 1.9 4h-3.8c.4-1.5 1.1-2.8 1.9-4zM4.3 14a8 8 0 0 1 0-4h3.4a16 16 0 0 0 0 4zm.8 2h3a15 15 0 0 0 1.3 3.9A8 8 0 0 1 5.1 16zm3-8h-3a8 8 0 0 1 4.3-3.9A15 15 0 0 0 8.1 8zM12 20c-.8-1.2-1.5-2.5-1.9-4h3.8c-.4 1.5-1.1 2.8-1.9 4zm2.3-6H9.7a14 14 0 0 1 0-4h4.6a14 14 0 0 1 0 4zm.3 5.9a15 15 0 0 0 1.3-3.9h3a8 8 0 0 1-4.3 3.9zm1.7-5.9a16 16 0 0 0 0-4h3.4a8 8 0 0 1 0 4z"/></svg>
        hargreavehomeholdings.co.uk
      </li>
    </ul>
  </section>

  <section class="card card--back">
    <div class="scene" role="img" aria-label="Photo of a sunny apartment terrace with palm plants and neighbouring buildings, tinted teal"></div>
    <div class="brand">HARGREAVE</div>
    <p class="services">Property<span class="dot"></span>Buy<span class="dot"></span>Sell<span class="dot"></span>Lettings<span class="dot"></span>Invest</p>
  </section>

</body>
</html>
```